Medical group practice

We need a flyer design incorporating the three doctors in the practice, there is a general practitioner, ophthalmologist and an obstetrician & Gynaecologist. see the attached file for the concept. will leave the colour design up to you

Target Market(s)

general public

Industry/Entity Type

Health Care

Colors

Designer to choose colors to be used in the design.

Requirements
Must have
• logos included in attachement

```html
<!DOCTYPE html>
<html lang="en">
<head>
<meta charset="utf-8">
<title>VitalCare Medical Flyer</title>
<link rel="stylesheet" href="https://fonts.googleapis.com/css2?family=Merriweather:wght@900&family=Oswald:wght@500&family=Arimo:wght@400;700&family=Roboto+Condensed:wght@400;700&family=Montserrat:wght@800&family=Didact+Gothic&family=Noto+Serif:ital,wght@1,700&display=swap">
<style>
:root{
  --frame:#5b4ea3;
  --red:#ed1c24;
  --grey:#77787b;
  --sky:#6dcff6;
  --cream:#fff6b8;
  --band:#5a4aa0;
  --yellow:#fff200;
  --ink:#1a1a1a;
  --orange:#f15a22;
  --magenta:#e6197f;
  --gold:#d49a12;
  --navy:#2e3192;
  --green:#00a651;
  --mail:#29abe2;
  --rule:#3a3a3a;
}
*{margin:0;padding:0;box-sizing:border-box}
html,body{width:1200px;height:1200px;overflow:hidden;background:#fff}
.canvas{position:relative;width:1200px;height:1200px;background:#fff}
.flyer{position:absolute;left:182px;top:62px;width:836px;height:1077px;border:2px solid var(--frame);overflow:hidden;background:#fff}
.abs{position:absolute}
.hero-photo{left:0;top:0;width:420px;height:360px;
  background:radial-gradient(ellipse at 30% 35%,#e9c9b4 0%,#dcc3b6 30%,rgba(235,232,236,.6) 60%,rgba(255,255,255,0) 80%);}
.hero-haze{left:180px;top:0;width:656px;height:140px;background:linear-gradient(180deg,#eceef2 0%,rgba(255,255,255,0) 100%)}
.brand{font-family:"Merriweather",serif;font-weight:900;line-height:1;text-align:center;white-space:nowrap}
.brand-top{left:228px;top:108px;width:532px;font-size:58px;color:var(--red);letter-spacing:-1px}
.brand-bottom{left:328px;top:170px;width:340px;font-size:58px;color:var(--grey);letter-spacing:1px}
.tagline{left:225px;top:229px;width:538px;height:51px;background:var(--sky);color:var(--cream);
  font-family:"Oswald",sans-serif;font-weight:500;font-size:35px;line-height:51px;text-align:center;white-space:nowrap}
.address{left:180px;top:288px;width:600px;font-family:"Arimo",sans-serif;font-weight:700;font-size:20px;line-height:28px;color:var(--ink);text-align:center;white-space:nowrap}
.phones{left:62px;top:352px;width:707px;height:81px;background:var(--band);color:#fff;
  font-family:"Roboto Condensed",sans-serif;font-size:23px;line-height:28px;text-align:center;padding-top:12px;white-space:nowrap}
.phones b{color:var(--yellow);font-weight:700}
.hours{left:62px;top:445px;height:36px;display:flex;align-items:center;font-family:"Arimo",sans-serif;white-space:nowrap}
.hours-label{background:var(--red);color:#fff;font-size:20px;height:36px;line-height:36px;padding:0 8px 0 10px}
.hours-text{font-size:22.5px;color:var(--ink);margin-left:6px;font-weight:400}
.rule{height:1.5px;background:var(--rule)}
.vrule{width:1px;background:var(--rule)}
.mark{font-family:"Didact Gothic",sans-serif;font-size:13px;color:var(--ink);display:flex;align-items:center;justify-content:center;gap:6px;text-align:center;white-space:nowrap}
.mark i{display:inline-block;width:12px;height:12px;border-radius:50%}
.doc-name{font-family:"Montserrat",sans-serif;font-weight:800;font-size:23px;text-align:center;line-height:1;white-space:nowrap}
.doc-role{font-family:"Didact Gothic",sans-serif;font-size:16px;letter-spacing:1px;color:var(--ink);text-align:center;line-height:19px;font-weight:700;white-space:nowrap}
.services{font-family:"Didact Gothic",sans-serif;font-size:15.8px;letter-spacing:.4px;color:var(--ink);line-height:23.3px;white-space:nowrap;font-weight:700}
.services em{font-style:normal;color:var(--red)}
.email{display:flex;align-items:center;gap:9px;font-family:"Noto Serif",serif;font-style:italic;font-weight:700;font-size:14px;letter-spacing:.6px;color:var(--ink);white-space:nowrap}
.email svg{flex:none}
.ob-row{font-family:"Didact Gothic",sans-serif;font-size:15px;letter-spacing:.4px;color:var(--ink);line-height:18px;font-weight:700;white-space:nowrap}
.ob-label-blue{color:var(--navy)}
.ob-label-green{color:var(--green)}
</style>
</head>
<body>
<div class="canvas">
  <div class="flyer">
    <div class="abs hero-haze"></div>
    <div class="abs hero-photo" role="img" aria-label="Photo of a doctor's hand holding a stethoscope toward the viewer"></div>

    <div class="abs brand brand-top">VITALCARE</div>
    <div class="abs brand brand-bottom">MEDICAL</div>
    <div class="abs tagline">- Your Health is our Priority -</div>
    <div class="abs address">42 Harbour Road, Port Linden, St. Avery<br>Tel : (555) 410 2280 / 2281</div>

    <div class="abs phones">
      General Practitioner - <b>(555) 320 4417</b> • Ophthalmologist - <b>(555) 320 8852</b><br>
      Obstetrician/Gynaecologist – <b>(555) 320 6193, (555) 610 7745</b>
    </div>

    <div class="abs hours"><span class="hours-label">Opening hours :</span><span class="hours-text">Monday – Fridays 9am-6pm | Saturdays 10am – 5pm</span></div>
    <div class="abs rule" style="left:62px;top:495px;width:712px"></div>
    <div class="abs vrule" style="left:416px;top:509px;height:257px"></div>

    <!-- General practitioner -->
    <div class="abs mark" style="left:60px;top:530px;width:280px"><i style="background:#1b75bc;border-radius:2px"></i>Ashworth Care</div>
    <div class="abs doc-name" style="left:40px;top:577px;width:320px;color:var(--orange)">Dr. Kelvin Ashworth</div>
    <div class="abs doc-role" style="left:40px;top:603px;width:300px">MD. General Practitioner</div>
    <div class="abs rule" style="left:61px;top:629px;width:319px;height:1px"></div>
    <div class="abs services" style="left:66px;top:634px">
      General Checks &nbsp;| Annual Check ups<br>
      Wound Care/Dressings | Incision &amp; Drainage<br>
      Suturing lacerations | Pain Injections<br>
      Glucose checks | Foreign Body Removal
    </div>
    <div class="abs rule" style="left:61px;top:733px;width:319px;height:1px"></div>
    <div class="abs email" style="left:64px;top:740px">
      <svg width="30" height="30" viewBox="0 0 30 30"><circle cx="15" cy="15" r="13.5" fill="none" stroke="var(--mail)" stroke-width="1.5"/><rect x="8" y="10" width="14" height="10" fill="none" stroke="var(--mail)" stroke-width="1.3"/><path d="M8 10l7 6 7-6M8 20l5-4.5M22 20l-5-4.5" fill="none" stroke="var(--mail)" stroke-width="1.3"/></svg>
      kelvin.ashworth.md@mailbox.com
    </div>

    <!-- Ophthalmologist -->
    <div class="abs mark" style="left:460px;top:555px;width:300px;color:#7a2a8c"><i style="background:#92278f"></i>Clearview Eye Services</div>
    <div class="abs doc-name" style="left:430px;top:579px;width:360px;color:var(--magenta)">Dr. Lucinda R. Varela</div>
    <div class="abs doc-role" style="left:430px;top:604px;width:360px">MD. Surgeon Ophthalmologist</div>
    <div class="abs rule" style="left:443px;top:629px;width:319px;height:1px"></div>
    <div class="abs services" style="left:456px;top:634px">
      Eyes disease examination<br>
      Surgery of Pterygium | Cataract,<br>
      Glaucoma | <em>Emergency:</em> Conjunctivitis<br>
      Traumatism | Foreign body and more
    </div>
    <div class="abs rule" style="left:443px;top:733px;width:323px;height:1px"></div>
    <div class="abs email" style="left:443px;top:740px">
      <svg width="30" height="30" viewBox="0 0 30 30"><circle cx="15" cy="15" r="13.5" fill="none" stroke="var(--mail)" stroke-width="1.5"/><rect x="8" y="10" width="14" height="10" fill="none" stroke="var(--mail)" stroke-width="1.3"/><path d="M8 10l7 6 7-6M8 20l5-4.5M22 20l-5-4.5" fill="none" stroke="var(--mail)" stroke-width="1.3"/></svg>
      lucinda.eyes@mailbox.com
    </div>
    <div class="abs rule" style="left:62px;top:780px;width:712px"></div>

    <!-- Obstetrician & Gynaecologist -->
    <div class="abs mark" style="left:268px;top:800px;width:300px"><i style="background:var(--green)"></i>Mehrotra Women's Health</div>
    <div class="abs doc-name" style="left:268px;top:840px;width:300px;color:var(--gold)">Dr. Anil Mehrotra</div>
    <div class="abs doc-role" style="left:218px;top:863px;width:400px;line-height:18px">BMedSci, MBBS, DM (O&amp;G), FACOG<br>Obstetrician &amp; Gynaecologist</div>
    <div class="abs rule" style="left:49px;top:903px;width:734px;height:1px"></div>
    <div class="abs ob-row" style="left:110px;top:910px"><span class="ob-label-blue">Obstetrics</span></div>
    <div class="abs ob-row" style="left:222px;top:910px">:</div>
    <div class="abs ob-row" style="left:242px;top:910px">Prenatal Care | Delivery, Postnatal checks | High Risk pregnancy</div>
    <div class="abs ob-row" style="left:110px;top:938px"><span class="ob-label-green">Gynaecology</span></div>
    <div class="abs ob-row" style="left:222px;top:938px">:</div>
    <div class="abs ob-row" style="left:242px;top:938px">Pap smears | Abnormal vaginal bleeding | Fibroids | Colposcopy<br>Family planning | Infertility | Cancer screening, And More....</div>
    <div class="abs rule" style="left:72px;top:982px;width:688px;height:1px;background:#999"></div>
    <div class="abs email" style="left:310px;top:988px">
      <svg width="30" height="30" viewBox="0 0 30 30"><circle cx="15" cy="15" r="13.5" fill="none" stroke="var(--mail)" stroke-width="1.5"/><rect x="8" y="10" width="14" height="10" fill="none" stroke="var(--mail)" stroke-width="1.3"/><path d="M8 10l7 6 7-6M8 20l5-4.5M22 20l-5-4.5" fill="none" stroke="var(--mail)" stroke-width="1.3"/></svg>
      docmehrotra@mailbox.com
    </div>
    <div class="abs rule" style="left:49px;top:1023px;width:734px;height:1px"></div>
  </div>
</div>
</body>
</html>
```